nutrition ebook cover

i need a cover for a ebook designed, the book is called Amber Lattice so i would like that somewhere on the cover. i would also like the word nutrition followed by my company logo that i have attached below somewhere on the cover( i have attached two logos and would like to see with both separatley), i would like this to be faded into the background if possible, perhaps in a upper or lower corner. i would also like to see options with and without the picture i have attached below. the look I'm going for is professional and clean. this is a fat loss, healthy eating booklet. the winning designer i would like to design the following pages within the book aswell no more than 10 pages, that i will provide all content for, i just need help with putting what i have on pdf in a way that looks professional and cool. this would ideally covered in the rate that is paid for the cover. i also have other booklets i need made so the winning designer will most likely get that work too at a later date for an additional fee of course.

Industry/Entity Type

Nutrition

Requirements
Nice to have
• Outside images are welcomed, happy to purchase any stock images used from a outside source

```html
<!DOCTYPE html>
<html lang="en">
<head>
<meta charset="UTF-8">
<title>Amber Lattice — Ebook Cover</title>
<link href="https://fonts.googleapis.com/css2?family=Anton&family=Playfair+Display:wght@400&display=swap" rel="stylesheet">
<style>
  :root {
    --board-warm: #c0652f;
    --board: #7a4529;
    --board-dark: #4a2c1b;
    --slate: #2e3a39;
    --slate-deep: #1f2a28;
    --ink-light: #ffffff;
    --mark-faint: rgba(35, 20, 12, 0.42);
    --mark-ghost: rgba(255, 255, 255, 0.3);
  }
  * { margin: 0; padding: 0; box-sizing: border-box; }
  html, body { width: 800px; height: 1200px; overflow: hidden; background: var(--slate-deep); }
  .cover { position: relative; width: 800px; height: 1200px; overflow: hidden; }

  .food-photo {
    position: absolute; inset: 0;
    background: linear-gradient(100deg,
      var(--board-warm) 0%,
      var(--board) 30%,
      var(--board-dark) 55%,
      var(--slate) 72%,
      var(--slate-deep) 100%);
  }

  .title-main {
    position: absolute; left: 50px; top: 350px;
    font-family: "Anton", sans-serif; font-size: 200px; line-height: 1;
    text-transform: uppercase; letter-spacing: 2px; color: var(--ink-light);
  }
  .title-sub {
    position: absolute; left: 48px; top: 628px;
    font-family: "Playfair Display", serif; font-size: 130px; line-height: 1;
    color: var(--ink-light);
  }

  .brand-stamp {
    position: absolute; left: 54px; top: 880px;
    display: flex; align-items: center; gap: 14px;
    font-family: "Playfair Display", serif; font-size: 30px; color: var(--mark-faint);
  }
  .brand-stamp .dot {
    width: 30px; height: 30px; border-radius: 50%; background: var(--mark-faint);
  }
  .brand-ghost {
    position: absolute; right: 36px; bottom: 48px;
    font-family: "Playfair Display", serif; font-size: 42px; color: var(--mark-ghost);
  }
</style>
</head>
<body>
  <main class="cover">
    <div class="food-photo" role="img" aria-label="Overhead photo of a rustic wooden cutting board on a dark slate table surrounded by fresh vegetables: broccoli, carrot, cherry tomatoes, mushrooms, lemon, rocket leaves, olive oil and a pepper mill"></div>

    <h1 class="title">
      <span class="title-main">Amber</span>
      <span class="title-sub">Lattice</span>
    </h1>

    <div class="brand-stamp"><span class="dot"></span><span>Fieldstone Nutrition</span></div>
    <div class="brand-ghost">Fieldstone Nutrition</div>
  </main>
</body>
</html>
```